Bramble Harbor Foundation Web Design

The design we need is for a WordPress blog that will be our content platform. We are a registered 501(c)3 non-profit that focuses on financially supporting the treatment of cancer patients that have been told they have no hope and there is nothing the conventional medical system can do for them. Through this wesbite we want to both rasie awareness about the treatment options plus, raise funds for treating patients. The two primary target audiences of the site are...

1. Terminally ill patients and their families to let them know that there is an option other then hospice and that we are hear to support that option.

2. People looking to help donate to a worthwhile cause that resonates with them.

The website is https://brambleharborfoundation.org/

See attached logo designs!!!

Target Market(s)

Cancer patients and their families

Industry/Entity Type

Foundation

Font styles to use
Sans Serif

Colors
ffffff
fbed22

Requirements
Must have
• I like this look of this site. It is clean, simple, helpful, soft. I like the flow of the pages.
• http://www.quietmeadowtrust.org/
• I like the design and flow but NOT the color or boldness
• https://tmvq-youth.org/
• I like this style for a donation page.
• https://www.curewaveaid.org/about-cwa/stand-with-us/gifts/single-gift
• with the addition of a Would you like your employer to match? button.
Nice to have
• White black and gold - but soft
• Even possibly grayscale like the site I like.

```html
<!DOCTYPE html>
<html lang="en">
<head>
<meta charset="utf-8">
<title>Bramble Harbor Foundation</title>
<link href="https://fonts.googleapis.com/css2?family=Roboto:wght@300;400;500;700&display=swap" rel="stylesheet">
<style>
:root{
  --gold:#eccb55;
  --yellow:#f9e825;
  --ink:#1d1d1d;
  --muted:#555;
  --grey-band:#e4e4e4;
  --white:#ffffff;
  --dark-bar:#2b2b2b;
}
*{box-sizing:border-box;margin:0;padding:0}
html,body{width:1200px;height:1200px;overflow:hidden;background:var(--white);font-family:'Roboto',sans-serif;color:var(--ink)}
.page{position:relative;width:1200px;height:1200px}
.abs{position:absolute}
.hero-photo{left:0;top:0;width:1200px;height:402px;background:linear-gradient(100deg,#c9c4bf 0%,#b8a89a 30%,#d8cfc6 55%,#c7a98c 75%,#e0dad4 100%)}
.topbar{left:0;top:0;width:1200px;height:93px;background:rgba(120,120,120,.55)}
.brand{left:132px;top:50px;color:var(--white);font-size:15px;font-weight:500;letter-spacing:.5px;display:flex;align-items:center;gap:8px}
.brand .dot{width:14px;height:14px;border-radius:50%;background:var(--gold)}
.phone{left:970px;top:8px;color:var(--white);font-size:15px;display:flex;align-items:center;gap:8px}
.nav{top:51px;color:var(--white);font-size:12.5px}
.nav.active{color:var(--yellow)}
.hero-title{left:306px;top:216px;width:586px;height:65px;background:rgba(255,255,255,.72);font-size:30px;font-weight:300;text-align:center;line-height:65px}
.hero-sub{left:300px;top:286px;width:600px;text-align:center;font-size:16px}
.dots{left:577px;top:359px;display:flex;gap:7px}
.dots span{width:9px;height:9px;border-radius:50%;background:#111}
.dots span.on{background:var(--white);border:1px solid var(--gold)}
.h2{font-size:24px;font-weight:400;text-align:center}
.h2 b{color:var(--gold);font-weight:400}
.mark{width:60px;height:1px;background:var(--gold);margin:4px auto 0;position:relative}
.mark::after{content:"";position:absolute;left:22px;top:-7px;border-left:8px solid transparent;border-right:8px solid transparent;border-bottom:7px solid var(--gold)}
.mark.dark{background:var(--ink);width:60px}
.mark.dark::after{border-bottom-color:var(--ink)}
.about-text{left:132px;top:456px;width:620px;font-size:12.6px;line-height:16px;color:#222}
.btn{display:flex;align-items:center;justify-content:center;gap:8px;font-size:12px;border:2px solid var(--gold);background:var(--white)}
.btn-outline{border:2px solid var(--white);background:transparent}
.btn-dark{border:2px solid var(--ink);background:transparent}
.raise{left:771px;top:417px;width:297px;height:149px;background:linear-gradient(135deg,#f3e35a,#eadc3a);text-align:center}
.raise h3{font-size:24px;font-weight:500;margin-top:16px}
.raise p{font-size:16px;font-weight:300}
.raise hr{border:0;border-top:1px dashed #555;width:256px;margin:6px auto 0}
.band{left:0;top:574px;width:1200px;height:197px;background:var(--grey-band)}
.card{width:215px;height:116px;top:639px;background:var(--gold)}
.card .ic{position:absolute;left:9px;top:9px;width:42px;height:42px;border-radius:50%;background:var(--yellow);display:flex;align-items:center;justify-content:center}
.card h4{position:absolute;left:60px;top:8px;font-size:16px;font-weight:400}
.card p{position:absolute;left:61px;top:29px;font-size:12px;line-height:16px;color:#555;width:150px}
.card .btn{position:absolute;left:62px;top:69px;width:91px;height:35px}
.event-photo{left:132px;top:828px;width:456px;height:161px;background:linear-gradient(120deg,#c8c8d2,#8e95c9 55%,#c7c9d8)}
.event-card{left:150px;top:931px;width:416px;height:160px;background:#e9e9e9}
.date{left:167px;top:944px;width:62px;height:121px;background:var(--gold);text-align:center;font-size:16px;padding-top:56px;line-height:19px}
.blog-thumb{width:96px;height:96px;left:611px;background:linear-gradient(135deg,#efe07a,#e3d14f)}
.blog-title{left:722px;font-size:16px;font-weight:400}
.meta{left:721px;font-size:12px;color:#444;display:flex;gap:18px}
.blog-text{left:721px;width:350px;font-size:12px;line-height:16px;color:#555}
.footer{left:0;top:1108px;width:1200px;height:74px;background:var(--yellow);border-top:1px dashed #bbb}
.fh{font-size:12px;color:#222}
.fl{font-size:10px;line-height:13.5px;color:#333}
.input{background:var(--gold);font-size:9px;color:#888;padding:2px 5px}
.copy{left:0;top:1182px;width:1200px;height:18px;background:var(--dark-bar);color:#ccc;font-size:7.5px;padding:5px 0 0 133px}
</style>
</head>
<body>
<div class="page">
  <div class="abs hero-photo" role="img" aria-label="Photo of a smiling patient in a headscarf with a caring young woman beside her"></div>
  <div class="abs topbar"></div>
  <div class="abs brand"><span class="dot"></span>Bramble Harbor Foundation</div>
  <div class="abs phone"><svg width="10" height="15" viewBox="0 0 10 15"><rect x="1" y="1" width="8" height="13" rx="1.5" fill="none" stroke="#fff" stroke-width="1.5"/><circle cx="5" cy="11.5" r="1" fill="#fff"/></svg>0311 4400</div>
  <div class="abs nav active" style="left:518px">HOME</div>
  <div class="abs nav" style="left:582px">ABOUT</div>
  <div class="abs nav" style="left:647px">EVENTS</div>
  <div class="abs nav" style="left:723px">TREATMENTS</div>
  <div class="abs nav" style="left:825px">DONATION</div>
  <div class="abs nav" style="left:914px">BLOG</div>
  <div class="abs nav" style="left:971px">CONTACT</div>
  <svg class="abs" style="left:1052px;top:52px" width="12" height="12" viewBox="0 0 12 12"><circle cx="5" cy="5" r="3.8" fill="none" stroke="#fff" stroke-width="1.8"/><line x1="8" y1="8" x2="11" y2="11" stroke="#fff" stroke-width="2"/></svg>
  <div class="abs hero-title">BRAMBLE HARBOR FOUNDATION</div>
  <div class="abs hero-sub">research and treatment of cancer patients</div>
  <div class="abs dots"><span class="on"></span><span></span><span></span></div>

  <div class="abs" style="left:211px;top:412px;width:200px"><div class="h2">WHO <b>WE ARE</b></div><div class="mark"></div></div>
  <p class="abs about-text">We are a registered 501(c)3 non-profit that focuses on financially supporting the research and treatment of cancer patients that have been told they have no hope and there is nothing the conventional medical system can do for them.</p>
  <div class="abs btn" style="left:132px;top:514px;width:91px;height:35px">Read More <span>»</span></div>
  <div class="abs raise">
    <h3>Raise funds</h3>
    <p>for treating patients</p>
    <hr>
    <div class="btn btn-dark" style="width:125px;height:35px;margin:22px auto 0;font-size:16px;font-weight:300">Donate us <span>»</span></div>
  </div>

  <div class="abs band"></div>
  <div class="abs" style="left:300px;top:585px;width:600px"><div class="h2" style="font-size:25px;font-weight:300">AWARENESS&nbsp; <span style="font-weight:500">ABOUT THE TREATMENT OPTIONS</span></div><div class="mark dark"></div></div>

  <div class="abs card" style="left:132px"><div class="ic"><svg width="24" height="20" viewBox="0 0 24 20"><line x1="3" y1="17" x2="20" y2="4" stroke="#111" stroke-width="3"/><rect x="2" y="12" width="5" height="7" fill="#111"/></svg></div><h4>OPTION-1</h4><p>Lorem ipsum dolor sit amet, consectetur adipiscing elit,</p><div class="btn btn-outline">DETAILS <span>»</span></div></div>
  <div class="abs card" style="left:372px"><div class="ic"><svg width="16" height="22" viewBox="0 0 16 22"><path d="M8 1 C8 1 1 10 1 14 a7 7 0 0 0 14 0 C15 10 8 1 8 1z" fill="#111"/><rect x="7" y="10" width="2" height="6" fill="#f9e825"/></svg></div><h4>OPTION-2</h4><p>Lorem ipsum dolor sit amet, consectetur adipiscing elit,</p><div class="btn btn-outline">DETAILS <span>»</span></div></div>
  <div class="abs card" style="left:612px"><div class="ic"><svg width="22" height="22" viewBox="0 0 22 22"><rect x="3" y="6" width="16" height="8" rx="4" transform="rotate(40 11 10)" fill="#111"/><circle cx="9" cy="19" r="1.2" fill="#111"/><circle cx="13" cy="19" r="1.2" fill="#111"/></svg></div><h4>OPTION-3</h4><p>Lorem ipsum dolor sit amet, consectetur adipiscing elit,</p><div class="btn btn-outline">DETAILS <span>»</span></div></div>
  <div class="abs card" style="left:853px"><div class="ic"><svg width="24" height="22" viewBox="0 0 24 22"><rect x="2" y="12" width="20" height="4" fill="#111"/><rect x="2" y="8" width="2" height="13" fill="#111"/><rect x="20" y="12" width="2" height="9" fill="#111"/><circle cx="12" cy="5" r="3" fill="#111"/></svg></div><h4>OPTION-4</h4><p>Lorem ipsum dolor sit amet, consectetur adipiscing elit,</p><div class="btn btn-outline">DETAILS <span>»</span></div></div>

  <div class="abs" style="left:263px;top:782px;width:200px"><div class="h2">NEW <b>EVENTS</b></div><div class="mark"></div></div>
  <div class="abs event-photo" role="img" aria-label="Photo of a doctor beside a patient in a treatment scanner"></div>
  <div class="abs event-card"></div>
  <div class="abs date"><svg style="position:absolute;left:16px;top:14px" width="30" height="30" viewBox="0 0 30 30"><rect x="2" y="5" width="26" height="23" fill="none" stroke="#fff" stroke-width="2.5"/><line x1="2" y1="11" x2="28" y2="11" stroke="#fff" stroke-width="2.5"/><path d="M8 16h14M8 21h14M12 13v13M18 13v13" stroke="#fff" stroke-width="1.5"/></svg>28<sup style="font-size:8px">th</sup><br><b style="font-weight:500">DEC</b><br>2017</div>
  <div class="abs" style="left:250px;top:939px;width:290px;text-align:center;font-size:15.5px">LOREM IPSUM DOLOR SIT</div>
  <div class="abs" style="left:372px;top:962px;width:32px;height:2px;background:#111"></div>
  <div class="abs" style="left:248px;top:973px;font-size:12.5px;color:#444">◷ 10:00 AM - 3:00 PM</div>
  <div class="abs" style="left:410px;top:973px;font-size:12.5px;color:#444">⚲ 20, Newyork City,</div>
  <p class="abs" style="left:248px;top:997px;width:300px;font-size:12px;line-height:16px;color:#555">Lorem ipsum dolor sit amet, consectetur adipiscing elit, sed do eiusmod tempor incididunt ut labore et dolore</p>
  <div class="abs" style="left:246px;top:1054px;font-size:12.5px;color:#444">▣ $1,20,000 (Donated)</div>
  <div class="abs btn btn-dark" style="left:461px;top:1040px;width:90px;height:35px">DETAILS <span>»</span></div>

  <div class="abs" style="left:750px;top:782px;width:200px"><div class="h2">OUR <b>BLOG</b></div><div class="mark"></div></div>
  <div class="abs blog-thumb" style="top:829px" role="img" aria-label="Photo of a smiling patient with yellow tint"></div>
  <div class="abs blog-title" style="top:827px">LOREM IPSUM DOLOR SIT</div>
  <div class="abs meta" style="top:852px"><span>👤 Admin</span><span>💬 Comments (5)</span><span>📅 28th Dec, 2017</span></div>
  <p class="abs blog-text" style="top:872px">Lorem ipsum dolor sit amet, consectetur adipiscing elit, sed do eiusmod tempor incididunt ut labore et dolore magna aliqua. Ut</p>
  <div class="abs btn" style="left:721px;top:913px;width:104px;height:33px">VIEW MORE <span>»</span></div>
  <div class="abs" style="left:618px;top:961px;width:450px;border-top:1px dashed #ccc"></div>
  <div class="abs blog-thumb" style="top:973px" role="img" aria-label="Photo of a smiling patient with yellow tint"></div>
  <div class="abs blog-title" style="top:971px">LOREM IPSUM DOLOR SIT</div>
  <div class="abs meta" style="top:996px"><span>👤 Admin</span><span>💬 Comments (5)</span><span>📅 28th Dec, 2017</span></div>
  <p class="abs blog-text" style="top:1016px">Lorem ipsum dolor sit amet, consectetur adipiscing elit, sed do eiusmod tempor incididunt ut labore et dolore magna aliqua. Ut</p>
  <div class="abs btn" style="left:721px;top:1057px;width:104px;height:33px">VIEW MORE <span>»</span></div>

  <div class="abs footer"></div>
  <div class="abs fh" style="left:133px;top:1118px;font-weight:500">Bramble Harbor</div>
  <div class="abs fl" style="left:133px;top:1140px;line-height:16px;font-size:10.5px">Lorem ipsum dolor sit amet,<br>consectetur adipiscing elit, sed</div>
  <div class="abs fh" style="left:371px;top:1110px">QUICK LINKS</div>
  <div class="abs fl" style="left:372px;top:1124px">Home<br>About<br>Events<br>Treatments</div>
  <div class="abs fl" style="left:454px;top:1124px">Donation<br>Blog<br>Contact</div>
  <div class="abs fh" style="left:613px;top:1110px">GET IN TOUCH</div>
  <div class="abs fl" style="left:613px;top:1124px">⚲&nbsp; 14 Lantern Way,<br>&nbsp;&nbsp;&nbsp;&nbsp;Maplestead,02240, USA<br>☎&nbsp; 03100 4400<br>✉&nbsp; hello@bramble</div>
  <div class="abs fh" style="left:774px;top:1110px">QUICK CONTACT</div>
  <div class="abs input" style="left:774px;top:1128px;width:134px;height:17px">Name</div>
  <div class="abs input" style="left:933px;top:1128px;width:135px;height:17px">Email</div>
  <div class="abs input" style="left:774px;top:1149px;width:134px;height:28px">Message</div>
  <div class="abs fl" style="left:1022px;top:1164px;font-size:10px">SUBMIT »</div>
  <div class="abs copy">Copyright@ http://brambleharborfoundation.org, 2017 | All Rights Reserved</div>
  <div class="abs" style="left:990px;top:1186px;display:flex;gap:9px">
    <span style="width:9px;height:9px;background:#ccc"></span><span style="width:9px;height:9px;background:#ccc"></span><span style="width:9px;height:9px;background:#ccc"></span><span style="width:9px;height:9px;background:#ccc"></span>
  </div>
</div>
</body>
</html>
```